Stoneline Benchworks Australia - Pool Flyer

G'day,Stoneline Benchworks Australia sells poolforms (https://www.stonelinebenchworksaustralia.com.au/index.php?route=product/category&path=17_61) The poolforms are reusable forms to pour a seamless concrete pool surround instead of using coping tiles. A much better look, less maintenance, and a modern architectural look .We're going to attend a pool and spa show but it is also about landscaping/surround as well. The forms we do make the concrete surround of a pool instead of tiles. I've put some text in a word doc and pictures as well. Feel free to use any words from our website and use/crop pics as you see fit.Any questions, more than happy to answer. We're thinking an A4 tri-fold flyer but happy for other suggestions as well. We're going to attend the show, speak to exhibitors, and hand them the flyer (and maybe a little promo thing too).

Target Market(s)

The target market is we are going to a pool and spa expo. The exhibitors install pools and do backyard landscaping. The flyer is for them.

Colors

Designer to choose colors to be used in the design.

Requirements
Must have
• The text/description of the poolforms and some of the pictures.
• Finished pictures.
• 1 or 2 of the forms (From the website).
• 1 of the Veil skimmer cap pictures (finished is probably better from the jpg with 3 images. probably best to crop and use 1 of the 3.
• Contact details of the website & email contact of sales@stonelinebenchworksaustralia.com.au + the phone number.

```html
<!DOCTYPE html>
<html lang="en">
<head>
<meta charset="utf-8">
<title>Stoneline Benchworks Australia – Pool Flyer</title>
<link href="https://fonts.googleapis.com/css2?family=Montserrat:wght@300;400;500;600;700&family=Oswald:wght@300;400;500&display=swap" rel="stylesheet">
<style>
:root{
  --board:#a3a3a3;
  --ink:#1e1e1e;
  --band-dark:#2b2b2b;
  --band-mid:#6b6b6b;
  --grey-head:#999;
  --grey-text:#8a8a8a;
  --navy:#2a2160;
  --paper:#ffffff;
  --paper-shade:#e6e6e6;
  --pool:#2f43b8;
  --pool-deep:#1c2a86;
  --deck:#d9d4c9;
  --lawn:#4a6436;
  --frame:#cfcfcf;
}
*{margin:0;padding:0;box-sizing:border-box}
html,body{width:766px;height:1200px;overflow:hidden}
body{background:var(--board);font-family:'Montserrat',sans-serif;color:var(--ink);position:relative}
.abs{position:absolute}
.spread{position:absolute;left:40px;width:689px;height:487px;background:var(--band-mid);box-shadow:0 2px 6px rgba(0,0,0,.35);overflow:hidden}
.spread--outside{top:62px}
.spread--inside{top:618px}
.board-label{position:absolute;left:47px;font-size:24px;font-weight:400;color:#111;letter-spacing:.5px}
.card{position:absolute;background:linear-gradient(180deg,var(--paper) 0%,#f3f3f3 55%,var(--paper-shade) 100%)}
.footer-band{position:absolute;top:460px;height:20px;width:230px;color:#fff;font-size:7.4px;letter-spacing:1px;display:flex;align-items:center;justify-content:center}
.footer-band--dark{background:var(--band-dark)}
.footer-band--mid{background:var(--band-mid)}
.brand{position:absolute;display:flex;align-items:center;gap:8px}
.brand-dot{width:26px;height:26px;border-radius:50%;background:var(--ink)}
.brand-name{border-left:1px solid var(--ink);padding-left:7px;font-size:7.6px;line-height:11.5px;letter-spacing:3.2px;font-weight:400}
.brand--light .brand-dot{background:#fff}
.brand--light .brand-name{border-color:#fff;color:#fff;font-size:10.5px;line-height:16.5px;letter-spacing:4px}
.photo{position:absolute;overflow:hidden}
.photo-circle{position:absolute;border-radius:50%;border:7px solid #fff;box-shadow:0 1px 4px rgba(0,0,0,.25)}
.tick-list{position:absolute;list-style:none}
.tick-list li{position:relative;padding-left:20px;font-size:7.1px;line-height:9.4px;margin-bottom:6.5px}
.tick-list li::before{content:"";position:absolute;left:0;top:0;width:7px;height:7px;border:1.3px solid var(--ink);border-radius:50%}
.panel-title-light{font-size:15px;font-weight:400;color:var(--grey-head);line-height:18px}
.panel-title-bold{font-size:16px;font-weight:700;color:var(--grey-text);line-height:18px}
.body-copy{font-size:7.1px;line-height:9.4px}
.about-copy{font-size:6.9px;line-height:9.85px;text-align:justify;letter-spacing:-.05px}
.product-frame{position:absolute;width:86px;height:90px;border:1.5px solid var(--frame);background:linear-gradient(150deg,#ffffff 0%,#f4f4f4 30%,#dcdcdc 46%,#fbfbfb 56%,#e2e2e2 72%,#ffffff 100%)}
.product-info{position:absolute;width:112px}
.product-name{font-size:8.8px;font-weight:700;line-height:11.5px;margin-bottom:6px}
.product-desc{font-size:7.2px;line-height:9.8px;text-align:justify;margin-bottom:7px}
.price{font-size:7.6px;font-weight:700;line-height:10px}
.price-ex{font-size:7.3px;line-height:10px}
.muted{color:#9a9a9a}
</style>
</head>
<body>

<!-- ===== OUTSIDE SPREAD ===== -->
<section class="spread spread--outside">
  <div class="card" style="left:12px;top:12px;width:218px;height:448px;border-top-left-radius:12px;overflow:hidden">
    <div class="photo" role="img" aria-label="Kidney shaped blue pool with exposed aggregate concrete surround and umbrella" style="left:0;top:318px;width:218px;height:130px;background:linear-gradient(180deg,rgba(30,30,34,.85) 0%,rgba(30,30,34,0) 35%),linear-gradient(90deg,#3f5a34 0%,#c9c4ba 25%,#bdb8ae 100%)">
      <div class="abs" style="left:30px;top:52px;width:160px;height:70px;border-radius:50% 50% 45% 45%;background:radial-gradient(ellipse at 50% 40%,#3d5fd0,var(--pool-deep) 80%)"></div>
    </div>
    <svg class="abs" style="left:0;top:300px" width="218" height="30" viewBox="0 0 218 30"><path d="M0 0 H218 V10 Q120 34 0 12 Z" fill="#eaeaea"/><path d="M0 12 Q120 34 218 10 V14 Q120 38 0 16Z" fill="#d8d8d8"/></svg>
  </div>
  <div class="brand" style="left:32px;top:28px"><span class="brand-dot"></span><span class="brand-name">STONELINE<br>BENCHWORKS<br>AUSTRALIA</span></div>
  <div class="abs" style="left:30px;top:73px;width:200px">
    <div class="panel-title-light">THE BEST SEAMLESS</div>
    <div class="panel-title-bold">POOLEDGE FORMING<br>SYSTEM</div>
  </div>
  <p class="abs body-copy" style="left:29px;top:134px;width:176px">Don't waste your time with fiddly, flimsy, or time consuming pool edge forming systems that end up in landfill. The Edge Poolforms are made from strong PVC and can produce architectural designed looks that suit all types of pools.</p>
  <div class="abs panel-title-bold" style="left:30px;top:201px;font-size:15px;color:#a5a5a5">ADVANTAGES</div>
  <ul class="tick-list" style="left:30px;top:227px;width:180px">
    <li>Easy to use to create a seamless pooledge</li>
    <li>An average sized pool can be formed up and ready to for pouring in 2 hours</li>
    <li>Forms are resusable and do not addto landfill</li>
    <li>Made from tough PVC</li>
    <li>Forms are both straight and bendable so no problem for any shaped pool</li>
  </ul>

  <div class="abs" style="left:230px;top:12px;width:229px;height:475px;background:var(--paper)"></div>
  <div class="abs" style="left:251px;top:26px;font-size:14px;font-weight:700">GET IN TOUCH WITH US</div>
  <div class="abs" style="left:251px;top:45px;font-size:7.6px">to get your hands on the best pool formwork.</div>
  <ul class="tick-list" style="left:251px;top:67px;width:200px">
    <li style="margin-bottom:5.5px">Form and pour a seamless concrete pool surround</li>
    <li style="margin-bottom:5.5px">Architectural-designed look</li>
    <li style="margin-bottom:5.5px">Virtually no maintenance</li>
    <li style="margin-bottom:5.5px">Any Type of Concrete - Honed Aggregate, Exposed Aggregate, Grey or any colour concrete</li>
    <li>Any Type of Pool - Fibreglass and concrete pools</li>
  </ul>
  <div class="photo-circle" role="img" aria-label="Close-up of polished concrete pool edge over blue water" style="left:278px;top:163px;width:124px;height:124px;background:linear-gradient(115deg,#c9d3dc 0%,#6f8fb4 22%,#2d6fc8 40%,#1f5bb8 60%,#47a0dc 80%,#2c62b0 100%)"></div>
  <div class="brand" style="left:280px;top:310px"><span class="brand-dot"></span><span class="brand-name">STONELINE<br>BENCHWORKS<br>AUSTRALIA</span></div>
  <svg class="abs" style="left:311px;top:366px" width="80" height="18" viewBox="0 0 80 18">
    <circle cx="9" cy="9" r="8" fill="#1e1e1e"/><path d="M9 4.5a3 3 0 0 1 3 3c0 2.2-3 5.5-3 5.5s-3-3.3-3-5.5a3 3 0 0 1 3-3z" fill="#fff"/><circle cx="9" cy="7.5" r="1.1" fill="#1e1e1e"/>
    <circle cx="33" cy="9" r="8" fill="#1e1e1e"/><path d="M29.5 5.5l2-1 1.4 2.4-1.2 1a6 6 0 0 0 2.4 2.4l1-1.2 2.4 1.4-1 2c-3.5.2-7.2-3.5-7-7z" fill="#fff"/>
    <circle cx="57" cy="9" r="8" fill="#1e1e1e"/><rect x="52.5" y="6" width="9" height="6.5" rx="1" fill="#fff"/><path d="M52.8 6.4l4.2 3.2 4.2-3.2" stroke="#1e1e1e" stroke-width=".9" fill="none"/>
  </svg>
  <div class="abs" style="left:230px;top:391px;width:229px;text-align:center">
    <div style="font-size:9.3px;font-weight:600;line-height:12px">Stoneline Benchworks Australia</div>
    <div style="font-size:9px;font-weight:300;line-height:12px">Kelvale Victoria, Australia</div>
    <div style="font-size:11px;font-weight:700;margin-top:8px">1300 555 019</div>
    <div style="font-size:6.9px;margin-top:8px">sales@stonelinebenchworksaustralia.com.au</div>
  </div>

  <div class="abs" style="left:459px;top:0;width:230px;height:460px;background:linear-gradient(180deg,#0c0c0c 0%,#1a1a1a 48%,#dcdcdc 62%,#f6f6f6 100%)"></div>
  <div class="brand brand--light" style="left:489px;top:30px"><span class="brand-dot" style="width:42px;height:42px"></span><span class="brand-name">STONELINE<br>BENCHWORKS<br>AUSTRALIA</span></div>
  <div class="abs" style="left:460px;top:106px;width:228px;height:228px;border-radius:50%;background:#fff"></div>
  <div class="photo" role="img" aria-label="Rectangular blue pool with seamless white concrete surround and outdoor furniture" style="left:480px;top:126px;width:188px;height:188px;border-radius:50%;background:linear-gradient(180deg,#1c1f22 0%,#2c302b 20%,#4f6a3a 28%,#d9d6cf 34%,#e3e0da 40%,#3a52c8 46%,#2b3fb4 70%,var(--pool-deep) 100%)"></div>
  <div class="abs" style="left:459px;top:357px;width:230px;text-align:center;font-family:'Oswald',sans-serif;color:#222">
    <div style="font-size:20px;font-weight:300;letter-spacing:3px;line-height:26px">THE BEST SEAMLESS</div>
    <div style="font-size:29px;font-weight:400;line-height:33px">POOLEDGE FORMING</div>
    <div style="font-size:29px;font-weight:400;line-height:33px;color:var(--navy)">SYSTEM</div>
  </div>

  <div class="footer-band footer-band--dark" style="left:0">www.stonelinebenchworksaustralia.com.au</div>
  <div class="footer-band footer-band--mid" style="left:230px;width:229px">www.stonelinebenchworksaustralia.com.au</div>
  <div class="footer-band footer-band--dark" style="left:459px">www.stonelinebenchworksaustralia.com.au</div>
</section>
<div class="board-label" style="top:565px">BROCHURE OUTSIDE</div>

<!-- ===== INSIDE SPREAD ===== -->
<section class="spread spread--inside">
  <div class="card" style="left:12px;top:12px;width:677px;height:448px;border-top-left-radius:12px;background:linear-gradient(90deg,#f4f4f4,#fff 20%,#ececec 32%,#f7f7f7 34%,#fff 60%,#efefef 66%,#fbfbfb 100%)"></div>
  <div class="photo" role="img" aria-label="Long blue pool with exposed aggregate surround, lawn, dark fence and outdoor lounge" style="left:0;top:300px;width:689px;height:160px;background:linear-gradient(180deg,#232427 0%,#2e3034 30%,rgba(46,48,52,0) 45%),linear-gradient(90deg,var(--lawn) 0%,#5b7640 8%,#c3beb4 14%,var(--pool) 22%,#2a3db0 55%,#c9c4ba 62%,var(--deck) 75%,#ebe7df 100%)"></div>
  <svg class="abs" style="left:0;top:290px" width="689" height="120" viewBox="0 0 689 120" preserveAspectRatio="none">
    <path d="M0 0 H689 V40 Q640 50 600 70 Q500 60 440 52 Q330 30 230 22 Q110 30 0 92 Z" fill="#f5f5f5"/>
  </svg>
  <div class="brand" style="left:26px;top:28px"><span class="brand-dot" style="width:36px;height:36px"></span><span class="brand-name" style="font-size:9px;line-height:14px;letter-spacing:3.8px">STONELINE<br>BENCHWORKS<br>AUSTRALIA</span></div>
  <div class="abs" style="left:25px;top:79px;font-size:18px;font-weight:700;color:#a5a5a5">ABOUT US</div>
  <p class="abs about-copy" style="left:24px;top:109px;width:186px">Stoneline Benchworks Australia (SBA) is Australia and New Zealands only appointed distributer of the Counterform and Poolform products from Benchform Solutions. We provide an online channel for this patented and award winning Edge Counterform decorative edge forms, concrete stains, sealers, and polishes. The product has been designed to make it easy to quickly create fantastic concrete countertops and poolforms at a lower total cost.</p>
  <p class="abs about-copy" style="left:24px;top:204px;width:186px">We look forward to hearing about your project and will be more than happy to help where we can.</p>
  <div class="abs" style="left:12px;top:235px;width:218px;text-align:center;font-size:8.6px;font-weight:600;line-height:12px">Stoneline Benchworks Australia Pty Ltd<br>ABN 42 118 306 574</div>
  <div class="photo-circle" role="img" aria-label="Veil skimmer cap set in exposed aggregate concrete" style="left:52px;top:275px;width:132px;height:132px;background:linear-gradient(150deg,#cfcac2 0%,#a9a49b 35%,#8c877f 55%,#b7b2a9 75%,#9a958c 100%)"></div>

  <div class="abs" style="left:230px;top:12px;width:459px;height:35px;background:var(--band-dark);border-bottom-left-radius:18px;color:#fff;font-size:15px;letter-spacing:13.5px;display:flex;align-items:center;justify-content:center;padding-left:60px">POOL&nbsp;FORMS</div>

  <div class="product-frame" role="img" aria-label="White PVC square poolform backing profile" style="left:242px;top:72px"></div>
  <div class="product-info" style="left:338px;top:74px">
    <div class="product-name">Square Poolform<br>Backing (8 pack)</div>
    <div class="product-desc">The Square Poolform Backing is a reusable PVC form which can be used to create a square profile inst..</div>
    <div class="price muted">$419.10</div><div class="price-ex muted">Ex Tax: $381.00</div>
  </div>

  <div class="product-frame" role="img" aria-label="White bendable PVC poolform strip" style="left:471px;top:72px"></div>
  <div class="product-info" style="left:567px;top:74px;width:114px">
    <div class="product-name" style="white-space:nowrap;font-size:8.4px;letter-spacing:-.2px;margin-bottom:5px">Bendable Edge Poolform</div>
    <div class="product-desc">Edge Poolform™ is a reusable PVC form used to create decorative concrete copings for swiming pools. Int..</div>
    <div class="price">$729.30</div><div class="price-ex">Ex Tax: $663.00</div>
  </div>

  <div class="product-info" style="left:242px;top:197px;width:110px">
    <div class="product-name">Edge Poolforms</div>
    <div class="product-desc">Edge Poolform™ is a reusable PVC form used to create decorative concrete copings for swiming pools. Int..</div>
    <div class="price muted">$601.70</div><div class="price-ex muted">Ex Tax: $547.00</div>
  </div>
  <div class="product-frame" role="img" aria-label="Straight white PVC poolform length" style="left:362px;top:190px"></div>

  <div class="product-info" style="left:471px;top:197px;width:105px">
    <div class="product-name">Receiver Track</div>
    <div class="product-desc" style="text-align:left">The Edge Poolform™ Receiver Track is used to mount the Poolform on top of the pool wall of a concrete o..</div>
    <div class="price">$291.50</div><div class="price-ex">Ex Tax: $265.00</div>
  </div>
  <div class="product-frame" role="img" aria-label="White PVC receiver track strip" style="left:590px;top:190px"></div>

  <div class="photo-circle" role="img" aria-label="Drinks and champagne chilling in a recessed concrete pool edge" style="left:281px;top:310px;width:124px;height:124px;background:linear-gradient(160deg,#6d737a 0%,#8f959c 30%,#a8acb0 50%,#7c8288 75%,#9a9ea2 100%)"></div>
  <div class="photo-circle" role="img" aria-label="Water rippling over a seamless concrete pool edge" style="left:505px;top:324px;width:132px;height:132px;background:linear-gradient(170deg,#1d2f48 0%,#2f4a6e 30%,#6f88a6 50%,#3a5578 70%,#22384f 100%)"></div>

  <div class="footer-band footer-band--dark" style="left:0">www.stonelinebenchworksaustralia.com.au</div>
  <div class="footer-band footer-band--mid" style="left:230px;width:229px">www.stonelinebenchworksaustralia.com.au</div>
  <div class="footer-band footer-band--dark" style="left:459px">www.stonelinebenchworksaustralia.com.au</div>
</section>
<div class="board-label" style="top:1122px">BROCHURE INSIDE</div>

</body>
</html>
```